Brochure Design

We need a 6 page Brochure designed for our product, please see attached document for more information. The content should focus on account work.

Target Market(s)

Businesses that use a taxi service for their business

Requirements
Must have
• Must have key content on the services we provide for Account work

```html
<!DOCTYPE html>
<html lang="en">
<head>
<meta charset="utf-8">
<title>Brochure Spread – Pages 4 &amp; 5</title>
<link href="https://fonts.googleapis.com/css2?family=Montserrat:ital,wght@0,300;0,400;0,500;0,600;1,300&display=swap" rel="stylesheet">
<style>
:root{
  --stage:#070d1a;
  --paper:#ffffff;
  --ink:#222a33;
  --muted:#3c454f;
  --gold:#f7b90f;
  --gold-line:#f5c334;
  --card:#fde8b3;
  --teal:#3fb8b0;
  --phone-edge:#c9ced4;
  --map:#dcdad4;
  --cancel:#f0595b;
}
*{box-sizing:border-box;margin:0;padding:0}
html,body{width:1200px;height:1200px;overflow:hidden;background:var(--stage);font-family:"Montserrat",sans-serif;color:var(--ink)}
.stage-title{position:absolute;top:118px;left:0;width:1200px;text-align:center;color:#fff;font-weight:300;font-size:30px;letter-spacing:.5px}
.spread{position:absolute;left:90px;top:224px;width:1022px;height:722px;background:var(--paper)}
.page-left{position:absolute;left:0;top:0;width:510px;height:722px;overflow:hidden}
.street-photo{position:absolute;inset:0;background:linear-gradient(100deg,#ffffff 0%,#f6f7f8 35%,#e2e0dc 60%,#cfcbc4 80%,#b8bcc0 100%)}
.street-photo::after{content:"";position:absolute;inset:0;background:linear-gradient(180deg,rgba(255,255,255,0) 55%,rgba(205,228,238,.7) 100%)}
.fold{position:absolute;left:509px;top:0;width:2px;height:722px;background:#1b2230}
.feature{position:absolute;left:0;width:290px;text-align:center}
.feature svg{display:block;margin:0 auto}
.feature h2{font-weight:400;font-size:15.5px;margin:6px 0 6px;color:var(--ink)}
.feature p{font-size:8.4px;line-height:12px;color:var(--muted);padding:0 66px}
.city-art{position:absolute;left:38px;top:544px;width:204px;height:132px;border-radius:10px;background:radial-gradient(ellipse at 50% 60%,#bfe6ee 0%,#dff1f4 60%,rgba(255,255,255,0) 100%)}
.site-url{position:absolute;left:31px;top:682px;font-size:8px;font-weight:600;color:var(--gold)}
.rule{position:absolute;left:94px;top:686px;width:896px;height:1px;background:var(--gold-line)}
.service{position:absolute;left:315px;width:150px;text-align:center;font-size:8.4px;font-weight:600;line-height:10.5px;color:var(--ink)}
.service svg{display:block;margin:0 auto 4px}
.page-right{position:absolute;left:510px;top:0;width:512px;height:722px}
.step{position:absolute;background:var(--card);border:1px solid var(--gold-line);border-radius:16px}
.step-text{position:absolute;font-size:8.8px;line-height:12px;color:var(--ink)}
.step-text.right{text-align:right}
.step-icon{position:absolute;width:22px;height:22px;border-radius:50%;background:var(--gold);display:flex;align-items:center;justify-content:center}
.phone{position:absolute;width:100px;height:209px;background:#fff;border:2px solid var(--phone-edge);border-radius:14px}
.phone .cam{position:absolute;top:10px;left:34px;width:4px;height:4px;border-radius:50%;background:#333}
.phone .spk{position:absolute;top:11px;left:44px;width:16px;height:2px;background:#333;border-radius:1px}
.phone .home{position:absolute;bottom:6px;left:41px;width:16px;height:16px;border-radius:50%;border:1.5px solid #555}
.screen{position:absolute;left:5px;top:26px;width:86px;height:157px;background:var(--map);overflow:hidden}
.bar{height:16px;background:var(--gold);font-size:5px;font-weight:500;color:#333;display:flex;align-items:center;padding-left:18px;position:relative}
.bar::before{content:"";position:absolute;left:5px;top:4px;width:8px;height:8px;border-radius:50%;background:#333}
.map{position:absolute;left:0;right:0;background:linear-gradient(135deg,#e3e1da,#cfcdc6 60%,#d8d6cf)}
.map.green{background:linear-gradient(160deg,#d5e5c8 0%,#e6e3d8 45%,#a9c6e6 70%,#d9e6cc 100%)}
.sheet{position:absolute;left:0;right:0;background:#fff;font-size:4.5px;color:#444;padding:3px 6px;line-height:8px}
.btn{position:absolute;left:0;right:0;bottom:0;height:12px;font-size:4.5px;font-weight:600;color:#fff;display:flex;align-items:center;justify-content:center}
.btn.dark{background:#1f1f1f;color:var(--gold)}
.btn.red{background:var(--cancel)}
.download{position:absolute;left:0;width:512px;top:574px;text-align:center;font-weight:300;font-style:italic;font-size:22px;line-height:24px;color:var(--ink)}
.store{position:absolute;top:646px;height:19px;background:#111;border-radius:3px}
.store-divider{position:absolute;left:257px;top:640px;width:1px;height:32px;background:#eee}
</style>
</head>
<body>
<div class="stage-title">Page 4 &amp; 5</div>

<div class="spread">
  <section class="page-left">
    <div class="street-photo" role="img" aria-label="Soft-focus photograph of a city street lined with stone buildings and taxis"></div>

    <div class="feature" style="top:32px">
      <svg width="52" height="50" viewBox="0 0 52 50"><circle cx="26" cy="17" r="11" fill="none" stroke="#2a3440" stroke-width="2"/><path d="M15 16a11 11 0 0 1 22 0" fill="var(--gold)" stroke="#2a3440" stroke-width="2"/><path d="M5 48c2-12 11-16 21-16s19 4 21 16z" fill="var(--teal)" stroke="#2a3440" stroke-width="2"/></svg>
      <h2>24/7 SUPPORT</h2>
      <p>Open a business account today and take advantage of our executive services outside of London: whether your business travel takes you across the London, Europe, UAE, or Asia.</p>
    </div>

    <div class="feature" style="top:200px">
      <svg width="54" height="52" viewBox="0 0 54 52"><path d="M27 4a14 14 0 0 0-14 14c0 10 14 24 14 24s14-14 14-24A14 14 0 0 0 27 4z" fill="#fff" stroke="#2a3440" stroke-width="2"/><circle cx="27" cy="18" r="6" fill="var(--gold)"/><path d="M4 50l8-12h30l8 12z" fill="var(--teal)" stroke="#2a3440" stroke-width="2"/></svg>
      <h2>Average 7 Min Pick Ups</h2>
      <p>Open a business account today and take advantage of our executive services outside of London: whether your business travel takes you across the London, Europe, UAE, or Asia.</p>
    </div>

    <div class="feature" style="top:378px">
      <svg width="54" height="52" viewBox="0 0 54 52"><rect x="3" y="4" width="46" height="34" rx="3" fill="#fff" stroke="#2a3440" stroke-width="2"/><rect x="3" y="4" width="46" height="7" fill="var(--teal)" stroke="#2a3440" stroke-width="2"/><circle cx="16" cy="22" r="5" fill="var(--teal)"/><path d="M28 20h15M28 26h15M28 32h10" stroke="#2a3440" stroke-width="2"/><rect x="32" y="36" width="20" height="12" rx="4" fill="var(--gold)" stroke="#2a3440" stroke-width="2"/></svg>
      <h2>Trained, Hand Picked Drivers</h2>
      <p>Open a business account today and take advantage of our executive services outside of London: whether your business travel takes you across the London, Europe, UAE, or Asia.</p>
    </div>

    <div class="city-art" role="img" aria-label="Line illustration of city buildings, map pins and a taxi"></div>
    <div class="site-url">www.vexa.cab</div>

    <div class="service" style="top:58px"><svg width="20" height="20" viewBox="0 0 20 20" fill="none" stroke="#2a3440" stroke-width="1.5"><path d="M3 11l8-8h6v6l-8 8z"/><circle cx="14" cy="6" r="1.2"/></svg>Cost effective service<br>with quality vehicles</div>
    <div class="service" style="top:132px"><svg width="24" height="18" viewBox="0 0 24 18" fill="none" stroke="#2a3440" stroke-width="1.5"><circle cx="6" cy="9" r="4"/><path d="M10 9h12M18 9v4M21 9v3"/></svg>Dedicated Access<br>via online system</div>
    <div class="service" style="top:202px"><svg width="20" height="20" viewBox="0 0 20 20" fill="none" stroke="#2a3440" stroke-width="1.5"><rect x="2" y="4" width="16" height="14"/><path d="M2 8h16M6 2v4M14 2v4M6 12h2M10 12h2M14 12h1M6 15h2M10 15h2"/></svg>Bookings can be<br>made quickly and simply</div>
    <div class="service" style="top:275px"><svg width="20" height="20" viewBox="0 0 20 20" fill="none" stroke="#2a3440" stroke-width="1.5"><path d="M5 3l3 4-2 2a9 9 0 0 0 5 5l2-2 4 3-2 3A14 14 0 0 1 2 5z"/></svg>Phone Support<br>when needed, 24x7</div>
    <div class="service" style="top:347px"><svg width="20" height="20" viewBox="0 0 20 20" fill="none" stroke="#2a3440" stroke-width="1.5"><rect x="2" y="4" width="16" height="14"/><path d="M2 8h16M6 2v4M14 2v4M5 11h10M5 14h10"/></svg>Advanced<br>Booking options</div>
    <div class="service" style="top:419px"><svg width="24" height="20" viewBox="0 0 24 20" fill="none" stroke="#2a3440" stroke-width="1.5"><rect x="1" y="1" width="6" height="6"/><rect x="9" y="1" width="6" height="6"/><rect x="17" y="1" width="6" height="6"/><rect x="7" y="11" width="8" height="8"/><path d="M9 15l2 2 3-4"/></svg>Regular repeat<br>scheduled Booking options</div>
    <div class="service" style="top:492px"><svg width="22" height="20" viewBox="0 0 22 20" fill="none" stroke="#2a3440" stroke-width="1.5"><path d="M2 12l18-9-6 15-3-6z"/></svg>Airport Transfers</div>
    <div class="service" style="top:553px"><svg width="24" height="20" viewBox="0 0 24 20" fill="none" stroke="#2a3440" stroke-width="1.5"><path d="M3 13l3-7h12l3 7v4H3z"/><circle cx="7" cy="17" r="1.5"/><circle cx="17" cy="17" r="1.5"/></svg>Mid-range to<br>Executive vehicles</div>
    <div class="service" style="top:616px"><svg width="22" height="22" viewBox="0 0 22 22"><circle cx="11" cy="11" r="10" fill="#2a3440"/><circle cx="11" cy="11" r="4" fill="#fff"/></svg>Your entry point to the<br>UK-wide Vexa network</div>
  </section>

  <div class="fold"></div>

  <section class="page-right">
    <div class="step" style="left:38px;top:38px;width:207px;height:233px"></div>
    <div class="phone" style="left:50px;top:50px"><span class="cam"></span><span class="spk"></span>
      <div class="screen"><div class="bar">Request Taxi</div>
        <div class="map" style="top:16px;height:80px" role="img" aria-label="Street map with pickup pin"></div>
        <div class="sheet" style="top:96px;height:49px">From<br>Your pickup address<br>To<br>Your drop-off address</div>
        <div class="btn dark">CONFIRM</div></div>
      <span class="home"></span></div>
    <div class="step-icon" style="left:160px;top:167px"><svg width="12" height="12" viewBox="0 0 20 20" fill="#fff"><path d="M5 2l3 5-2 2a9 9 0 0 0 5 5l2-2 5 3-2 4A15 15 0 0 1 1 5z"/></svg></div>
    <div class="step-text" style="left:160px;top:200px">Call a taxi<br>any time,<br>any place</div>

    <div class="step" style="left:267px;top:54px;width:207px;height:234px"></div>
    <div class="phone" style="left:280px;top:68px"><span class="cam"></span><span class="spk"></span>
      <div class="screen"><div class="bar">Request Confirmed</div>
        <div class="map" style="top:16px;height:129px" role="img" aria-label="Street map showing nearby taxis around the pickup point"></div>
        <div class="btn red">CANCEL</div></div>
      <span class="home"></span></div>
    <div class="step-icon" style="left:391px;top:157px"><svg width="12" height="12" viewBox="0 0 20 20" fill="#fff"><circle cx="10" cy="6" r="4"/><path d="M2 19c1-6 5-8 8-8s7 2 8 8z"/></svg></div>
    <div class="step-text" style="left:391px;top:188px">The Driver<br>accepts and<br>you receive<br>the Taxi details</div>

    <div class="step" style="left:38px;top:306px;width:207px;height:234px"></div>
    <div class="phone" style="left:135px;top:319px"><span class="cam"></span><span class="spk"></span>
      <div class="screen"><div class="bar">Taxi On Route</div>
        <div class="sheet" style="top:16px;height:8px;background:#222;color:var(--gold);text-align:center;line-height:3px">Your taxi is on its way</div>
        <div class="map" style="top:24px;height:96px" role="img" aria-label="Street map showing the taxi approaching"></div>
        <div class="sheet" style="top:120px;height:25px">Driver &nbsp; Car &nbsp; Plate</div>
        <div class="btn red">CANCEL</div></div>
      <span class="home"></span></div>
    <div class="step-icon" style="left:114px;top:423px"><svg width="12" height="12" viewBox="0 0 20 20" fill="#fff"><path d="M10 1a7 7 0 0 0-7 7c0 5 7 11 7 11s7-6 7-11a7 7 0 0 0-7-7zm0 10a3 3 0 1 1 0-6 3 3 0 0 1 0 6z"/></svg></div>
    <div class="step-text right" style="right:387px;top:452px">Watch your Taxi<br>on its way,<br>jump in and go<br>to your destination</div>

    <div class="step" style="left:267px;top:324px;width:207px;height:233px"></div>
    <div class="phone" style="left:361px;top:336px"><span class="cam"></span><span class="spk"></span>
      <div class="screen"><div class="bar">Passenger On Board</div>
        <div class="map green" style="top:16px;height:128px" role="img" aria-label="City map with river showing the route to the destination"></div>
        <div class="sheet" style="top:144px;height:13px;background:#222;color:#fff;line-height:5px">Arriving in 10 min</div></div>
      <span class="home"></span></div>
    <div class="step-icon" style="left:339px;top:451px"><svg width="12" height="12" viewBox="0 0 20 20" fill="#fff"><circle cx="10" cy="10" r="8"/><circle cx="10" cy="10" r="4" fill="var(--gold)"/></svg></div>
    <div class="step-text right" style="right:161px;top:480px">Best experience<br>with<br>Vexa App</div>

    <div class="download">Download the Vexa App<br>from your Smartphone today!</div>
    <div class="store" style="left:168px;width:63px" role="img" aria-label="App store download badge"></div>
    <div class="store-divider"></div>
    <div class="store" style="left:281px;width:67px" role="img" aria-label="App store download badge"></div>
  </section>

  <div class="rule"></div>
</div>
</body>
</html>
```